Sophrologist needs a cool signage at door entrance

I need signage for dr in sophrology based in Belgium (french speaking). The signed should capture the name the "Mireille Vansteelant" - "Naturopathe-Sophrologue-Reiki" and a catchphrase = (Healthy way of life)
« Fais du bien à ton corps, pour que ton âme ait envie d’y rester »
Requirements
Must have
- Hey,
Thats the instagram account for some inspiration www.instagram.com/mireille_zen_equilibre
Light colors, green, blue
Healthy way of life
Size is 45cm wide on 30 cm high
The signage will be placed in front off woof pannel

```html
<!DOCTYPE html>
<html lang="fr">
<head>
<meta charset="utf-8">
<title>Mireille Vansteelant – Naturopathe-Sophrologue-Reiki</title>
<link rel="stylesheet" href="https://fonts.googleapis.com/css2?family=Dancing+Script:wght@700&family=Open+Sans:wght@400&family=Comic+Neue:wght@400;700&display=swap">
<style>
  :root {
    --page-bg: #eef3ea;
    --paper: #f7f8f5;
    --forest: #1f5238;
    --leaf: rgba(79, 154, 95, 0.95);
    --leaf-mid: rgba(130, 190, 125, 0.6);
    --leaf-fade: rgba(169, 211, 160, 0);
    --gold-mid: rgba(214, 180, 90, 0.55);
    --gold-fade: rgba(217, 174, 60, 0);
    --wash-blue: #dcecef;
    --ink: #222222;
    --rule: #4a4a4a;
  }
  * { box-sizing: border-box; margin: 0; padding: 0; }
  html, body {
    width: 1200px;
    height: 1200px;
    overflow: hidden;
    background: var(--page-bg);
  }
  .sign {
    position: absolute;
    left: 30px;
    top: 220px;
    width: 1140px;
    height: 760px;
    background:
      radial-gradient(ellipse 340px 160px at 420px 650px, var(--wash-blue) 0%, transparent 70%),
      radial-gradient(ellipse 260px 200px at 1050px 160px, #e6f0dc 0%, transparent 70%),
      var(--paper);
    overflow: hidden;
  }
  .foliage {
    position: absolute;
    background: radial-gradient(ellipse closest-side at center, var(--leaf) 0%, var(--leaf-mid) 50%, var(--leaf-fade) 100%);
  }
  .foliage--golden {
    background: radial-gradient(ellipse closest-side at center, var(--leaf) 0%, var(--gold-mid) 55%, var(--gold-fade) 100%);
  }
  .foliage--top-left { left: -220px; top: -230px; width: 640px; height: 460px; }
  .foliage--top-center { left: 420px; top: -200px; width: 560px; height: 330px; }
  .foliage--top-right { right: -200px; top: -200px; width: 420px; height: 560px; }
  .foliage--left { left: -200px; top: 240px; width: 400px; height: 640px; }
  .foliage--bottom-left { left: 60px; bottom: -200px; width: 560px; height: 360px; }
  .foliage--bottom-right { right: -230px; bottom: -240px; width: 620px; height: 640px; }

  .sign__name {
    position: absolute;
    left: 0;
    width: 1192px;
    top: 152px;
    text-align: center;
    font-family: "Dancing Script", cursive;
    font-weight: 700;
    font-size: 96px;
    line-height: 1;
    color: var(--forest);
  }
  .sign__rule {
    position: absolute;
    left: 224px;
    top: 267px;
    width: 744px;
    height: 1px;
    background: var(--rule);
  }
  .sign__role {
    position: absolute;
    left: 0;
    width: 1192px;
    top: 294px;
    text-align: center;
    font-family: "Open Sans", sans-serif;
    font-size: 33px;
    color: var(--ink);
  }
  .sign__motto {
    position: absolute;
    left: 322px;
    top: 368px;
    width: 510px;
    height: 106px;
    background: var(--forest);
    border-radius: 14px 30px 18px 26px;
    display: flex;
    align-items: center;
    justify-content: center;
    font-family: "Comic Neue", sans-serif;
    font-weight: 700;
    font-size: 44px;
    color: #ffffff;
  }
  .sign__quote {
    position: absolute;
    left: 0;
    width: 1192px;
    top: 506px;
    text-align: center;
    font-family: "Comic Neue", sans-serif;
    font-weight: 700;
    font-size: 34px;
    line-height: 51px;
    color: var(--ink);
  }
</style>
</head>
<body>
  <main class="sign">
    <div class="foliage foliage--top-left" role="img" aria-label="Watercolour green leaves with gold line leaves"></div>
    <div class="foliage foliage--golden foliage--top-center" role="img" aria-label="Watercolour palm leaves and gold outlined leaf"></div>
    <div class="foliage foliage--top-right" role="img" aria-label="Watercolour green leaves with gold outlined leaf"></div>
    <div class="foliage foliage--left" role="img" aria-label="Watercolour green leafy branch"></div>
    <div class="foliage foliage--golden foliage--bottom-left" role="img" aria-label="Watercolour leaves with gold fern sprigs"></div>
    <div class="foliage foliage--bottom-right" role="img" aria-label="Watercolour palm leaves with gold fern sprigs"></div>

    <h1 class="sign__name">Mireille Vansteelant</h1>
    <div class="sign__rule"></div>
    <p class="sign__role">Naturopathe-Sophrologue-Reiki</p>
    <p class="sign__motto">Healthy way of life</p>
    <p class="sign__quote">Fais du bien à ton corps,<br>pour que ton âme ait envie d’y rester</p>
  </main>
</body>
</html>
```